Parlow Electrical Solar Energy Marketing Flyer

Seeking a flyer to market our electrical business - promoting solar energy systems. Will be used as print marketing.

Attached are similar examples in the industry, as well as current Parlow Electrical ads and our new "Parlow Electrical, Air & Solar" logo.

We would like the reverse side to have information relating to solar for business.

This flyer is to promote the solar arm of our business, however we also deliver electrical and air-conditioning services. If possible it would be great to have a small reference to our air-conditioning service on the front page.We also need to reference the we have finance available.
Updates

Project Deadline Extended Reason: Apologies - due to illness I had been unable to complete the required text copy for flyer. Please note any slight changes to brief and copy will be updated urgently today while I am back in the office. There are some great flyers catching our eye. Added Monday, July 18, 2016

Target Market(s)

Home and Business Owners

Industry/Entity Type

Solar Energy

Logo Text

Parlow Electrical, Air & Solar

Requirements
Must have
• Company logo, VRT installer logo, Moxanta Logo, phone number and all licences stated on the attached Parlow Electrical ad. Catchy, uncomplicated appearance. Colours and pics to compliment logo. Disclaimer
Nice to have
• Testimonial

```html
<!DOCTYPE html>
<html lang="en">
<head>
<meta charset="utf-8">
<title>Parlow Electrical, Air &amp; Solar – Solar Flyer</title>
<link rel="stylesheet" href="https://fonts.googleapis.com/css2?family=Roboto:wght@300;400;700;900&family=Roboto+Condensed:wght@300;400;700&display=swap">
<style>
  :root {
    --page-bg: #e9e6e1;
    --paper: #fbfbf8;
    --brand-blue: #1872b8;
    --deep-blue: #0f66ad;
    --cyan: #22bfee;
    --cyan-light: #7fd6f4;
    --ink-grey: #6f6f6f;
    --ink-dark: #4a4a4a;
    --ink-black: #1d1d1d;
    --white: #ffffff;
    --badge-orange: #f07f1e;
    --disclaimer: #1466a8;
  }
  * { margin: 0; padding: 0; box-sizing: border-box; }
  html, body { width: 1200px; height: 1200px; overflow: hidden; background: var(--page-bg); }
  .flyer {
    position: absolute; left: 167px; top: 40px;
    width: 866px; height: 1120px; overflow: hidden;
    background: var(--paper);
    font-family: "Roboto", Arial, sans-serif;
    box-shadow: 0 6px 24px rgba(0,0,0,0.18);
  }
  .flyer-art { position: absolute; inset: 0; }
  .about { position: absolute; left: 25px; top: 24px; width: 486px; }
  .about-title { font-weight: 700; font-size: 15px; color: var(--ink-dark); letter-spacing: 0.8px; margin-bottom: 6px; }
  .about-text {
    font-weight: 300; font-size: 16.5px; line-height: 26px; color: var(--ink-grey);
    letter-spacing: 1.3px; white-space: nowrap;
  }
  .about-text span { display: flex; justify-content: space-between; }
  .brand { position: absolute; left: 552px; top: 42px; display: flex; align-items: center; gap: 12px; }
  .brand-dot { width: 44px; height: 44px; border-radius: 50%; background: var(--brand-blue); flex: none; }
  .brand-name { font-weight: 900; font-size: 25px; line-height: 27px; color: var(--brand-blue); width: 240px; }
  .headline { position: absolute; left: 30px; top: 300px; color: var(--white); }
  .headline-lead { font-weight: 300; font-size: 32px; line-height: 36px; }
  .headline-main { font-weight: 700; font-size: 45px; line-height: 46px; color: var(--cyan); letter-spacing: 0.3px; }
  .headline-offer { font-family: "Roboto Condensed", Arial, sans-serif; font-weight: 700; font-size: 17px; margin-top: 2px; }
  .benefits {
    position: absolute; left: 472px; top: 309px; width: 380px;
    list-style: none; font-family: "Roboto Condensed", Arial, sans-serif;
    font-weight: 300; font-size: 19px; line-height: 23.6px; color: var(--ink-black);
    white-space: nowrap;
  }
  .benefits li { position: relative; padding-left: 17px; margin-bottom: 3px; }
  .benefits li::before {
    content: ""; position: absolute; left: 0; top: 9px; width: 7px; height: 7px;
    border-radius: 50%; background: var(--ink-dark);
  }
  .finance-offer { position: absolute; left: 392px; top: 616px; width: 160px; text-align: right; color: var(--ink-black); }
  .finance-deposit { font-weight: 400; font-size: 22px; line-height: 28px; padding-right: 16px; }
  .finance-name { font-weight: 400; font-size: 30px; line-height: 38px; }
  .finance-note { font-weight: 700; font-size: 14px; letter-spacing: -0.5px; }
  .finance-note u { text-underline-offset: 2px; }
  .finance-side {
    position: absolute; left: 828px; top: 748px; transform: rotate(-90deg); transform-origin: left top;
    font-family: "Roboto Condensed", Arial, sans-serif; font-weight: 300; font-size: 15px; color: var(--white);
    white-space: nowrap;
  }
  .testimonials { position: absolute; left: 25px; top: 820px; color: var(--white); }
  .testimonials-title { font-weight: 300; font-size: 21px; margin-bottom: 6px; }
  .testimonial { font-weight: 300; font-size: 13.2px; line-height: 17px; margin-bottom: 7px; letter-spacing: -0.2px; white-space: nowrap; }
  .disclaimer {
    position: absolute; left: 25px; top: 1044px;
    font-family: "Roboto Condensed", Arial, sans-serif; font-weight: 300;
    font-size: 13.4px; line-height: 17px; color: var(--disclaimer); white-space: nowrap;
  }
</style>
</head>
<body>
<main class="flyer">
  <svg class="flyer-art" width="866" height="1120" viewBox="0 0 866 1120">
    <defs>
      <linearGradient id="sky-field" x1="0" y1="0" x2="0.6" y2="1">
        <stop offset="0" stop-color="#e6f5fc"/>
        <stop offset="0.4" stop-color="#a3d3f2"/>
        <stop offset="0.7" stop-color="#4a7cc6"/>
        <stop offset="1" stop-color="#2a56a8"/>
      </linearGradient>
      <linearGradient id="field-grass" x1="0" y1="0" x2="0" y2="1">
        <stop offset="0" stop-color="#e6f1c4"/>
        <stop offset="1" stop-color="#a6cc3a"/>
      </linearGradient>
    </defs>
    <rect class="top-band" x="0" y="0" width="866" height="12" fill="var(--brand-blue)"/>
    <polygon class="cyan-field" points="0,264 337,288 866,130 866,1120 0,1120" fill="var(--cyan)"/>
    <g role="img" aria-label="Photo of rooftop solar panels under a bright blue sky above a green grass field">
      <polygon points="0,400 451,288 866,200 866,520 0,776" fill="url(#sky-field)"/>
      <polygon points="460,512 866,512 866,525 600,600" fill="url(#field-grass)"/>
    </g>
    <polygon class="lower-band" points="0,776 866,520 866,600 0,800" fill="var(--deep-blue)"/>
    <polygon class="headline-band" points="0,264 451,288 451,398 0,440" fill="var(--deep-blue)" opacity="0.93"/>
    <g class="finance-diamond">
      <polygon points="443,498 615,670 443,842 271,670" fill="var(--cyan-light)"/>
      <polygon points="443,514 599,670 443,826 287,670" fill="var(--cyan)"/>
      <polygon points="443,526 587,670 443,814 299,670" fill="var(--white)"/>
    </g>
    <g class="accreditation-diamond">
      <polygon points="685,672 877,864 685,1056 493,864" fill="var(--brand-blue)" opacity="0.35"/>
      <polygon points="685,700 849,864 685,1028 521,864" fill="var(--cyan)"/>
      <polygon points="685,706 843,864 685,1022 527,864" fill="var(--white)"/>
      <circle class="accreditation-badge" cx="644" cy="862" r="40" fill="var(--badge-orange)" role="img" aria-label="Accredited installer badge"/>
    </g>
  </svg>

  <section class="about">
    <h2 class="about-title">About Us:</h2>
    <p class="about-text">
      <span><i style="font-style:normal">We are a family owned business providing solar energy</i></span>
      <span>installations as well as air-conditioning and general</span>
      <span>electrical services throughout South East Queensland.</span>
      <span>Tom is our licenced electrician and solar energy designer</span>
      <span>&amp; installer with a depth of knowledge to better assist our</span>
      <span>customers. We pride ourselves on providing outstanding</span>
      <span>customer service, listening to customer needs and</span>
      <span style="display:block">assisting in providing the most efficient solutions.</span>
    </p>
  </section>

  <div class="brand">
    <span class="brand-dot"></span>
    <span class="brand-name">Parlow Electrical, Air &amp; Solar</span>
  </div>

  <header class="headline">
    <p class="headline-lead">Don’t waste your tax refund!</p>
    <h1 class="headline-main">INVEST IN SOLAR!</h1>
    <p class="headline-offer">5KW From $4000***+GST</p>
  </header>

  <ul class="benefits">
    <li>Solar for your Home, Solar for your business</li>
    <li>Invest in Solar</li>
    <li>Install solar power today &amp; start saving</li>
    <li>Say NO to rising power bills! Install Solar Today.</li>
    <li>Why not combine your solar installation with<br>new air-conditioning or electrical improvements<br>– Finance Available.</li>
    <li>Call us for a FREE quote</li>
  </ul>

  <div class="finance-offer">
    <p class="finance-deposit">$0* Deposit</p>
    <p class="finance-name">Moxanta</p>
    <p class="finance-note">NO INTEREST <u>EVER!</u></p>
  </div>

  <p class="finance-side">Finance Available**</p>

  <section class="testimonials">
    <h2 class="testimonials-title">TESTIMONIALS:</h2>
    <p class="testimonial">"We have been using Tom from Parlow Electrical and Trade<br>for over 3 years. We have found Tom to be extremely helpful and<br>willing to go that little bit further to ensure that the job is done properly.<br>Tom has always been competitively priced and the job is completed<br>on time. We wouldn't recommend anyone else!" -  Harlow Pastoral Co.</p>
    <p class="testimonial">"From initial contact to completion of the work, Parlow Electrical and Trade have been<br>excellent. Tom's work is professional, Tom communicates throughout the job<br>keeping the customer informed. We would use Parlow Electrical and Trade again and<br>recommend them to anyone requiring electrical, solar or airconditioning." – D.Renton</p>
  </section>

  <p class="disclaimer">*Continuing credit provided by Moxanta Pty Ltd. Fees (including Establishment Fee, Monthly Account<br>Keepingfees and Payment Processing fees), charges, terms, conditions and lending criteria apply. Other deposit<br>amounts may be required depending on purchase.All information correct at time of print. Subject to changes.</p>
</main>
</body>
</html>
```